Tender Scout Letterhead Design Project

We need a letterhead design for a consultancy business based in Australia.

Tender Scout is a unique business designed to assist with the complex and time consuming nature of selecting contractors, showing them what to do and reviewing quotes when it comes to body corporate and strata maintenance items such as painting, waterproofing, plumbing and electrical.

Target Market(s)

apartment managers

Industry/Entity Type

Business

Requirements
Must have
• must have logo and contact details

Tender Scout
82 Wallaroo Creek Road
Yandara, QLD 4571
Ph 07 5391 2846
Fax 07 5327 6018
Mobile 0438 917304

```html
<!DOCTYPE html>
<html lang="en">
<head>
<meta charset="utf-8">
<title>Tender Scout Letterhead</title>
<link rel="stylesheet" href="https://fonts.googleapis.com/css2?family=Open+Sans:wght@400;700&display=swap">
<style>
  :root {
    --backdrop: #e9e7e4;
    --paper: #ffffff;
    --brand-grey: #a5a7aa;
    --text-dark: #2b2b2b;
    --leaf-green: #8cc63f;
    --citrus-orange: #f58220;
  }
  * { margin: 0; padding: 0; box-sizing: border-box; }
  html, body {
    width: 1200px;
    height: 900px;
    overflow: hidden;
    background: var(--backdrop);
    font-family: "Open Sans", Arial, sans-serif;
  }
  .letterhead {
    position: absolute;
    left: 298px;
    top: 22px;
    width: 604px;
    height: 860px;
    background: var(--paper);
    box-shadow: 0 2px 10px rgba(0, 0, 0, 0.12);
    overflow: hidden;
  }
  .brand-name {
    position: absolute;
    left: 36px;
    top: 40px;
    font-size: 36px;
    font-weight: 700;
    letter-spacing: -0.5px;
    line-height: 1;
    color: var(--brand-grey);
  }
  .contact {
    position: absolute;
    left: 38px;
    top: 88px;
    font-style: normal;
    font-size: 10.5px;
    line-height: 15px;
    color: var(--text-dark);
  }
  .tagline {
    position: absolute;
    right: 24px;
    top: 53px;
    text-align: right;
    font-size: 11.5px;
    font-weight: 700;
    letter-spacing: 2.6px;
    line-height: 15px;
    color: var(--leaf-green);
  }
  .footer-waves {
    position: absolute;
    left: 0;
    bottom: 0;
    width: 604px;
    height: 110px;
    display: block;
  }
  .wave-green { fill: var(--leaf-green); }
  .wave-orange { fill: var(--citrus-orange); }
</style>
</head>
<body>
  <main class="letterhead">
    <div class="brand-name">Tender Scout</div>
    <address class="contact">
      82 Wallaroo Creek Road<br>
      Yandara, QLD 4571<br>
      Ph 07 5391 2846 | Fx 07 5327 6018 | Mb&nbsp; 0438 917304
    </address>
    <p class="tagline">KNOW EVERY QUOTE<br>BEFORE YOU SIGN</p>
    <svg class="footer-waves" viewBox="0 0 604 110" preserveAspectRatio="none" aria-hidden="true">
      <path class="wave-green" d="M0,54 Q300,96 604,14 L604,34 Q300,106 0,64 Z"/>
      <path class="wave-orange" d="M0,74 Q300,114 604,48 L604,110 L0,110 Z"/>
    </svg>
  </main>
</body>
</html>
```